New Automotive supply business in need of label designs for additive range

I need front and back label design for about 12 different variety of products. They are all to do with the Automotive additive industry such as Petrol injector cleaner, Engine Flush, Oil treatments etc. I will provide overall measurements of the label in the brief as well as examples of artwork that I like. Label must comply with local regulations, i can assist you with this. We will start with one product only, and if successful I am happy to hire you to do the remainder of the project. I would like to see designs that use my company logo colors. These products are for the workshop industry only (not retail) so does not have to be too animated.You will see my logo designs under the name "kalmor" in the uploaded files.Product Name is : Motor Prime & Renew
Front Label must say:PREPARES ENGINES FOR NEW OIL
RESTORES COMPRESSION
MINIMISES CONTAMINATION WITH NEW OIL
CONTAINS KALMOR TUFFLINE PROTECTION
RECOMMENDED FOR PETROL, DIESEL AND HYBRID ENGINES
350ML
Dimensions of metal can that will be used for label is : 175mm in height and 56mm in diameter. IN THE UPLOADED FILES YOU WILL SEE A SAMPLE OF THE ACTUAL CAN TO BE USED.
I have now included an example of a shield/guard that should be shown on the rear of the label if possible, im happy if you come up with your own shield designs.

Target Market(s)

Mechanics

Industry/Entity Type

Automotive Part

Requirements
Must have
• My logo on top
Nice to have
• Silver background
Should not have
• Pictures of engines or engine parts etc

```html
<!DOCTYPE html>
<html lang="en">
<head>
<meta charset="utf-8">
<title>Kalmor Motor Prime &amp; Renew – Can Label</title>
<link rel="stylesheet" href="https://fonts.googleapis.com/css2?family=Exo+2:ital,wght@0,800;1,800&family=Russo+One&family=Oswald:wght@500&family=Roboto:wght@400;700&family=Open+Sans:wght@400&display=swap">
<style>
  :root {
    --blue: #1d5fbf;
    --blue-dark: #14449a;
    --blue-light: #3a94e6;
    --navy: #0b1f44;
    --orange: #f07a1a;
    --silver-1: #c4c8cd;
    --silver-2: #ffffff;
    --silver-3: #dfe1e4;
    --ink: #1a1a1a;
    --white: #ffffff;
  }
  * { box-sizing: border-box; margin: 0; padding: 0; }
  html, body { width: 820px; height: 1200px; overflow: hidden; background: var(--white); }
  .canvas { position: relative; width: 820px; height: 1200px; overflow: hidden; background: var(--white); }

  .side-caption {
    position: absolute; top: 48px; width: 320px; text-align: center;
    font-family: "Open Sans", sans-serif; font-size: 40px; color: var(--ink);
  }
  .side-caption--front { left: 54px; }
  .side-caption--back { left: 442px; }

  .label { position: absolute; top: 142px; width: 316px; height: 989px; overflow: hidden; }
  .label--front { left: 56px; }
  .label--back { left: 443px; width: 318px; }
  .label-bg { position: absolute; inset: 0; width: 100%; height: 100%; }

  .brand { position: absolute; left: 0; right: 0; display: flex; flex-direction: column; align-items: center; }
  .brand-dot { border-radius: 50%; background: var(--blue); }
  .brand-name { font-family: "Exo 2", sans-serif; font-weight: 800; color: var(--blue); letter-spacing: 2px; }
  .label--front .brand { top: 96px; gap: 10px; }
  .label--front .brand-dot { width: 74px; height: 74px; }
  .label--front .brand-name { font-size: 40px; }
  .label--back .brand { top: 82px; gap: 6px; }
  .label--back .brand-dot { width: 46px; height: 46px; }
  .label--back .brand-name { font-size: 20px; }

  .product-title {
    position: absolute; left: 16px; top: 312px; transform: rotate(-12deg); transform-origin: left top;
    font-family: "Exo 2", sans-serif; font-weight: 800; line-height: 1;
  }
  .product-title .line-1 { display: block; font-size: 38px; color: var(--white); letter-spacing: 0.5px; }
  .product-title .line-2 {
    display: block; font-size: 46px; color: var(--navy); margin-top: 6px; margin-left: 4px;
    -webkit-text-stroke: 3px var(--white); paint-order: stroke fill;
  }
  .product-title .amp { color: var(--blue-light); font-size: 54px; }

  .tagline {
    position: absolute; left: 16px; top: 590px; transform: rotate(-14deg); transform-origin: left top;
    font-family: "Russo One", sans-serif; font-size: 27px; line-height: 1.05; color: var(--blue);
    -webkit-text-stroke: 3px var(--white); paint-order: stroke fill; text-align: center; width: 300px;
  }

  .benefits { position: absolute; left: 34px; top: 684px; list-style: none; }
  .benefits li {
    position: relative; padding-left: 26px; margin-bottom: 0;
    font-family: "Oswald", sans-serif; font-weight: 500; font-size: 18px; line-height: 33px; color: var(--white);
  }
  .benefits li::before {
    content: ""; position: absolute; left: 0; top: 11px; width: 10px; height: 10px; border-radius: 50%; background: var(--orange);
  }

  .volume {
    position: absolute; left: 0; right: 0; top: 924px; text-align: center;
    font-family: "Oswald", sans-serif; font-weight: 500; font-size: 30px; letter-spacing: 1px; color: var(--white);
  }

  .info { position: absolute; left: 34px; width: 252px; }
  .info h2 { font-family: "Roboto", sans-serif; font-weight: 700; font-size: 13px; color: var(--blue-dark); margin-bottom: 4px; }
  .info p { font-family: "Roboto", sans-serif; font-size: 8.6px; line-height: 12.5px; color: var(--blue); text-align: justify; }
  .info--application { top: 180px; }
  .info--features { top: 308px; }
  .info--directions { top: 436px; }

  .contact {
    position: absolute; left: 0; right: 0; top: 726px; text-align: center;
    font-family: "Roboto", sans-serif; color: var(--white); font-size: 10.5px; line-height: 15px;
  }
  .contact .website { font-weight: 700; font-size: 12px; margin-bottom: 6px; }
  .contact strong { font-weight: 700; }
  .contact .warning {
    display: inline-block; margin-top: 8px; padding: 2px 6px; font-weight: 700; font-size: 9.5px;
    border-left: 1px solid var(--white); border-right: 1px solid var(--white);
  }

  .cert-badges { position: absolute; left: 0; right: 0; top: 940px; display: flex; justify-content: center; gap: 12px; }
  .cert-badges span { width: 26px; height: 26px; border-radius: 50%; background: var(--white); }
</style>
</head>
<body>
<main class="canvas">
  <h1 class="side-caption side-caption--front">Front</h1>
  <h1 class="side-caption side-caption--back">Back</h1>

  <!-- FRONT LABEL -->
  <section class="label label--front">
    <svg class="label-bg" viewBox="0 0 316 989" preserveAspectRatio="none" aria-hidden="true">
      <defs>
        <linearGradient id="silverFront" x1="0" y1="0" x2="1" y2="0">
          <stop offset="0" stop-color="#c4c8cd"/><stop offset="0.35" stop-color="#ffffff"/>
          <stop offset="0.7" stop-color="#dfe1e4"/><stop offset="1" stop-color="#f4f5f6"/>
        </linearGradient>
        <linearGradient id="blueBand" x1="0" y1="0" x2="1" y2="0">
          <stop offset="0" stop-color="#1e63c4"/><stop offset="0.5" stop-color="#3a94e6"/><stop offset="1" stop-color="#1e63c4"/>
        </linearGradient>
        <linearGradient id="blueBody" x1="0" y1="0" x2="0" y2="1">
          <stop offset="0" stop-color="#2f83dc"/><stop offset="1" stop-color="#1a55b0"/>
        </linearGradient>
      </defs>
      <rect width="316" height="989" fill="url(#silverFront)"/>
      <rect y="10" width="316" height="6" fill="#f07a1a"/>
      <rect y="24" width="316" height="37" fill="url(#blueBand)"/>
      <polygon points="30,296 250,252 250,257 30,301" fill="#1d5fbf"/>
      <polygon points="0,318 200,278 200,282 0,322" fill="#14449a"/>
      <polygon points="0,345 316,278 316,395 0,465" fill="url(#blueBand)"/>
      <polygon points="0,465 316,395 316,989 0,989" fill="url(#blueBody)"/>
      <polygon points="0,520 316,452 316,460 0,528" fill="#ffffff"/>
      <polygon points="0,560 316,492 316,560 0,640" fill="#f07a1a"/>
      <polygon points="0,640 316,560 316,566 0,646" fill="#ffffff"/>
      <polygon points="20,672 300,610 300,614 20,676" fill="#14449a"/>
      <rect y="919" width="316" height="70" fill="#1b4fa8"/>
    </svg>

    <div class="brand">
      <span class="brand-dot"></span>
      <span class="brand-name">KALMOR</span>
    </div>

    <h2 class="product-title">
      <span class="line-1">MOTOR PRIME</span>
      <span class="line-2"><span class="amp">&amp;</span> RENEW</span>
    </h2>

    <p class="tagline">PREPARES ENGINES<br>FOR NEW OIL</p>

    <ul class="benefits">
      <li>RESTORES COMPRESSION</li>
      <li>MINIMISES CONTAMINATION<br>WITH NEW OIL</li>
      <li>CONTAINS KALMOR TUFFLINE<br>PROTECTION</li>
      <li>RECOMMENDED FOR PETROL,<br>DIESEL AND HYBRID ENGINES</li>
    </ul>

    <p class="volume">350ML</p>
  </section>

  <!-- BACK LABEL -->
  <section class="label label--back">
    <svg class="label-bg" viewBox="0 0 318 989" preserveAspectRatio="none" aria-hidden="true">
      <defs>
        <linearGradient id="silverBack" x1="0" y1="0" x2="1" y2="0">
          <stop offset="0" stop-color="#c4c8cd"/><stop offset="0.35" stop-color="#ffffff"/>
          <stop offset="0.7" stop-color="#dfe1e4"/><stop offset="1" stop-color="#f4f5f6"/>
        </linearGradient>
        <linearGradient id="blueBandBack" x1="0" y1="0" x2="1" y2="0">
          <stop offset="0" stop-color="#1e63c4"/><stop offset="0.5" stop-color="#3a94e6"/><stop offset="1" stop-color="#1e63c4"/>
        </linearGradient>
        <linearGradient id="blueBodyBack" x1="0" y1="0" x2="0" y2="1">
          <stop offset="0" stop-color="#2f83dc"/><stop offset="1" stop-color="#1a55b0"/>
        </linearGradient>
      </defs>
      <rect width="318" height="989" fill="url(#silverBack)"/>
      <rect y="10" width="318" height="6" fill="#f07a1a"/>
      <rect y="24" width="318" height="37" fill="url(#blueBandBack)"/>
      <polygon points="0,545 318,640 318,989 0,989" fill="url(#blueBodyBack)"/>
      <polygon points="0,552 200,612 200,617 0,557" fill="#14449a"/>
      <polygon points="110,590 318,652 318,660 110,597" fill="#ffffff"/>
      <polygon points="140,612 318,666 318,690" fill="#14449a"/>
      <rect y="919" width="318" height="70" fill="#1b4fa8"/>
    </svg>

    <div class="brand">
      <span class="brand-dot"></span>
      <span class="brand-name">KALMOR</span>
    </div>

    <div class="info info--application">
      <h2>APPLICATION</h2>
      <p>Lorem Ipsum is simply dummy text of the printing and typesetting industry. Lorem Ipsum has been the industry's standard dummy text ever since the 1500s, when an unknown printer took a galley of type and scrambled it to make a type specimen book. It has survived not only five centuries, but also the leap into electronic typesetting, remaining essentially unchanged.</p>
    </div>
    <div class="info info--features">
      <h2>FEATURES:</h2>
      <p>Lorem Ipsum is simply dummy text of the printing and typesetting industry. Lorem Ipsum has been the industry's standard dummy text ever since the 1500s, when an unknown printer took a galley of type and scrambled it to make a type specimen book. It has survived not only five centuries, but also the leap into electronic typesetting, remaining essentially unchanged.</p>
    </div>
    <div class="info info--directions">
      <h2>DIRECTIONS:</h2>
      <p>Lorem Ipsum is simply dummy text of the printing and typesetting industry. Lorem Ipsum has been the industry's standard dummy text ever since the 1500s, when an unknown printer took a galley of type and scrambled it to make a type specimen book. It has survived not only five centuries, but also the leap into electronic typesetting, remaining essentially unchanged.</p>
    </div>

    <div class="contact">
      <p>Visit our website:</p>
      <p class="website">www.kalmorsupply.net.au</p>
      <p><strong>Validity :</strong> 3 years</p>
      <p><strong>Product date:</strong> Please see can Bottom</p>
      <p class="warning">KEEP OOUT REACH OF CHILDREN</p>
    </div>

    <div class="cert-badges" aria-label="Certification badges">
      <span></span><span></span><span></span>
    </div>
  </section>
</main>
</body>
</html>
```